Online Fashion Boutique needs new Logo and Business Card Design

Veloa Boutique is a brand new boutique based in the UK.

We offer unique fashionable clothing, shoes and accessories for ladies.

For the design, I'll like a drawing/illustration of a fashionable lady with shopping bag(s) wearing heels and to the side "Veloa Boutique" under that "Keeping Style Unique". My preferred colours are Pink and Black and White(more like the Zebra print). I want the design to portray Stylish, Chic and Unique.

Boutique

```html
<!DOCTYPE html>
<html lang="en">
<head>
<meta charset="utf-8">
<title>Veloa Boutique – Business Cards</title>
<link rel="stylesheet" href="https://fonts.googleapis.com/css2?family=Playfair+Display:wght@400;700&family=Arimo:wght@400&display=swap">
<style>
  :root {
    --backdrop: #5fd0bf;
    --card: #f7f6f3;
    --card-edge: #d9efe8;
    --pink: #d0166f;
    --ink: #1e1e1e;
  }
  * { box-sizing: border-box; margin: 0; padding: 0; }
  html, body {
    width: 1200px;
    height: 1041px;
    overflow: hidden;
    background: var(--backdrop);
  }
  .canvas {
    position: relative;
    width: 1200px;
    height: 1041px;
  }
  .card {
    position: absolute;
    left: 290px;
    width: 620px;
    height: 354px;
    background: var(--card);
    border-bottom: 4px solid var(--card-edge);
    box-shadow: 0 14px 30px rgba(0, 60, 50, 0.22);
    overflow: hidden;
  }
  .card--front { top: 110px; }
  .card--back { top: 560px; }

  .brand {
    position: absolute;
    display: flex;
    align-items: center;
    gap: 12px;
    font-family: "Playfair Display", Georgia, serif;
    font-weight: 400;
    color: var(--pink);
    white-space: nowrap;
  }
  .brand__dot {
    width: 18px;
    height: 18px;
    border-radius: 50%;
    background: var(--pink);
    flex: none;
  }
  .card--front .brand {
    left: 52px;
    top: 74px;
    font-size: 40px;
  }
  .card--back .brand {
    left: 50%;
    top: 110px;
    transform: translateX(-50%);
    font-size: 44px;
  }

  .contact {
    position: absolute;
    left: 300px;
    top: 184px;
    font-family: "Arimo", Arial, sans-serif;
    color: var(--ink);
    font-size: 14px;
    line-height: 21px;
  }
  .contact__name {
    font-family: "Playfair Display", Georgia, serif;
    font-weight: 700;
    color: var(--pink);
    font-size: 22px;
    line-height: 30px;
    margin-bottom: 6px;
  }

  .card__website {
    position: absolute;
    left: 0;
    right: 0;
    top: 232px;
    text-align: center;
    font-family: "Arimo", Arial, sans-serif;
    font-size: 14px;
    letter-spacing: 0.5px;
    color: var(--pink);
  }
  .card__band {
    position: absolute;
    left: 0;
    right: 0;
    bottom: 38px;
    height: 28px;
    background: var(--pink);
  }
</style>
</head>
<body>
<main class="canvas">
  <section class="card card--front" aria-label="Business card front">
    <div class="brand">
      <span class="brand__dot"></span>
      <span class="brand__name">Veloa Boutique</span>
    </div>
    <div class="contact">
      <p class="contact__name">Name Surname</p>
      <p class="contact__phone">000 000 0000</p>
      <p class="contact__email">name@veloaboutique.com</p>
      <p class="contact__social">www.veloaboutique.com/community</p>
    </div>
  </section>

  <section class="card card--back" aria-label="Business card back">
    <div class="brand">
      <span class="brand__dot"></span>
      <span class="brand__name">Veloa Boutique</span>
    </div>
    <p class="card__website">www.veloaboutique.com</p>
    <div class="card__band"></div>
  </section>
</main>
</body>
</html>
```